Vesit cards for web development company

We need a business card design for our company. The company develops online platforms and conducts marketing consulting. Company logo. The cards must fit in with us (a junior start UP), but they must also be professional enough to impress with investors like banks. We wish you a combination of classic and modern design

Target Market(s)

Business partners and IT and marketing customers

Industry/Entity Type

It Company

Contact Information for Business Card

Folgende Information müssen Drauf.
Name, Position, Telefon Nr., Mobile Nr., E-Mail adresse, Optional sind noch Webadresse und HRB Nummer

Colors

Designer to choose colors to be used in the design.

Requirements
Must have
• The cards have to fit into the logo later and have to be dynamic and serious at the same time

```html
<!DOCTYPE html>
<html lang="en">
<head>
<meta charset="utf-8">
<title>Kelvo Development – Business Cards</title>
<link rel="stylesheet" href="https://fonts.googleapis.com/css2?family=Open+Sans:wght@400;600;700&display=swap">
<style>
  :root {
    --brand-blue: #1479c0;
    --brand-grey: #939598;
    --card-white: #f7f7f7;
    --ink-white: #ffffff;
    --ink-blue: #1a6fb5;
    --ink-navy: #1c4f86;
    --stage: #e9e7e4;
  }
  * { margin: 0; padding: 0; box-sizing: border-box; }
  html, body {
    width: 1200px; height: 900px; overflow: hidden;
    background: var(--stage);
    font-family: "Open Sans", Arial, sans-serif;
  }
  .stage { position: relative; width: 1200px; height: 900px; }

  .card { position: absolute; box-shadow: 0 6px 18px rgba(0,0,0,.18); overflow: hidden; }

  /* Front card */
  .card-front {
    left: 77px; top: 33px; width: 588px; height: 364px;
    background: var(--brand-blue); color: var(--ink-white);
  }
  .card-front .split { position: absolute; inset: 0; }
  .holder { position: absolute; left: 30px; top: 60px; }
  .holder-name { font-size: 19px; font-weight: 700; letter-spacing: .2px; line-height: 1.2; }
  .holder-role { font-size: 15px; font-weight: 400; margin-top: 2px; }
  .contacts { position: absolute; left: 30px; top: 226px; list-style: none; }
  .contacts li { display: flex; align-items: center; font-size: 15px; line-height: 21.5px; }
  .contacts svg { width: 13px; height: 13px; margin-right: 8px; fill: var(--ink-white); }
  .front-mark {
    position: absolute; left: 280px; width: 270px; top: 150px;
    text-align: center; font-size: 50px; font-weight: 700; letter-spacing: 2px;
    color: var(--ink-white); line-height: 1;
  }

  /* Back card */
  .card-back {
    left: 388px; top: 505px; width: 566px; height: 352px;
    background: var(--card-white); text-align: center;
  }
  .back-mark {
    position: absolute; left: 0; right: 0; top: 130px;
    font-size: 38px; font-weight: 700; color: var(--brand-blue);
    letter-spacing: 1px; line-height: 1.15;
  }
  .back-web {
    position: absolute; left: 0; right: 0; top: 293px;
    font-size: 14px; font-weight: 700; color: var(--ink-blue);
  }
  .back-web .tld { color: var(--ink-navy); }
</style>
</head>
<body>
<main class="stage">
  <section class="card card-front" aria-label="Business card front">
    <svg class="split" viewBox="0 0 588 364" preserveAspectRatio="none" aria-hidden="true">
      <path d="M363,0 Q140,182 378,364" fill="none" stroke="#7fb6e0" stroke-width="3"/>
      <path d="M365,0 Q142,182 380,364 L588,364 L588,0 Z" fill="var(--brand-grey)"/>
    </svg>
    <div class="holder">
      <p class="holder-name">MARCUS HALE</p>
      <p class="holder-role">Managing Director</p>
    </div>
    <ul class="contacts">
      <li><svg viewBox="0 0 16 16"><path d="M4 0h8a1 1 0 0 1 1 1v14a1 1 0 0 1-1 1H4a1 1 0 0 1-1-1V1a1 1 0 0 1 1-1zm1 2v10h6V2zm3 11a1 1 0 1 0 0 2 1 1 0 0 0 0-2z"/></svg>040-555 218 734</li>
      <li><svg viewBox="0 0 16 16"><path d="M1 5c0-2 3-3 7-3s7 1 7 3v1h-4V4.5H5V6H1zm2 2h10l1 7H2zm5 1.5a2.5 2.5 0 1 0 0 5 2.5 2.5 0 0 0 0-5z"/></svg>040-555 218 734</li>
      <li><svg viewBox="0 0 16 16"><path d="M0 3h16v10H0zm1.5 1.2V12h13V4.2L8 9z"/></svg>hello@kelvodev.com</li>
      <li><svg viewBox="0 0 16 16"><path d="M8 0a8 8 0 1 0 0 16A8 8 0 0 0 8 0zm-1 14.9A7 7 0 0 1 1.1 7H4l2 2v2l1 1zM9 1.1A7 7 0 0 1 14.9 8H12l-2-2V4L9 3z"/></svg>www.kelvodev.com</li>
    </ul>
    <p class="front-mark">KELVO</p>
  </section>

  <section class="card card-back" aria-label="Business card back">
    <p class="back-mark">KELVO<br>DEVELOPMENT</p>
    <p class="back-web">www.kelvodev<span class="tld">.com</span></p>
  </section>
</main>
</body>
</html>
```